Business Cards for accounting firm

Need a file and design that we can update for our employees when we get a design we like. Logo is attached.
Megan Tolliver CPA
Owner
P.O. Box 418
Perrysburg OH 43187
4193628405
megan@brightlanefin.com
www.brightlanefin.com
Accounting

```html
<!DOCTYPE html>
<html lang="en">
<head>
<meta charset="utf-8">
<title>Brightlane Financial — Business Card</title>
<link href="https://fonts.googleapis.com/css2?family=Raleway:wght@400;500;700&display=swap" rel="stylesheet">
<style>
  :root {
    --stage: #0e0e0f;
    --card: #323337;
    --blue: #29a8e0;
    --grey: #8a8b8e;
    --light: #e4e4e6;
  }
  * { margin: 0; padding: 0; box-sizing: border-box; }
  html, body {
    width: 1200px; height: 900px; overflow: hidden;
    background: var(--stage);
    font-family: "Raleway", sans-serif;
  }
  .canvas { position: relative; width: 1200px; height: 900px; }
  .card {
    position: absolute;
    background: var(--card);
    border-radius: 14px;
  }
  .card--front { left: 114px; top: 297px; width: 479px; height: 277px; }
  .card--back  { left: 634px; top: 299px; width: 469px; height: 275px; }

  .front-mark {
    position: absolute; left: 62px; top: 124px;
    display: flex; align-items: center; gap: 10px;
  }
  .front-mark__dot {
    width: 16px; height: 16px; border-radius: 50%; background: var(--blue);
  }
  .front-mark__name {
    color: var(--blue); font-weight: 700; font-size: 22px; letter-spacing: 0.2px;
  }

  .contact { position: absolute; left: 230px; top: 70px; color: var(--light); }
  .contact__name { font-size: 21px; font-weight: 500; color: var(--grey); line-height: 1.1; }
  .contact__first { color: var(--blue); }
  .contact__title { font-size: 14px; color: var(--grey); margin-top: 3px; }
  .contact__lines { margin-top: 16px; font-size: 14.5px; line-height: 18px; }
  .contact__label { color: var(--blue); }
  .contact__address { margin-top: 13px; font-size: 14.5px; line-height: 18px; }

  .back-mark {
    position: absolute; inset: 0;
    display: flex; align-items: center; justify-content: center;
  }
  .back-mark__name {
    color: var(--blue); font-weight: 700; font-size: 48px; line-height: 1.08; text-align: center;
  }
</style>
</head>
<body>
<main class="canvas">
  <section class="card card--front">
    <div class="front-mark">
      <span class="front-mark__dot"></span>
      <span class="front-mark__name">Brightlane</span>
    </div>
    <div class="contact">
      <p class="contact__name"><span class="contact__first">Megan</span> Tolliver</p>
      <p class="contact__title">Owner</p>
      <p class="contact__lines">
        <span class="contact__label">e:</span> megan@brightlanefin.com<br>
        <span class="contact__label">t:</span> 555-010-0142
      </p>
      <p class="contact__address">P.O. Box 418,<br>Perrysburg OH 43187</p>
    </div>
  </section>

  <section class="card card--back">
    <div class="back-mark">
      <p class="back-mark__name">Brightlane<br>Financial</p>
    </div>
  </section>
</main>
</body>
</html>
```